Business Card Design

Hoping for a black background business card, minimalistic design.
With the Marble Crest logo you created in white.

I would like to include:
My Name and title
Address (street address)
Reception: (phone number)
Fax: (fax number)
Reception: (email address)
Direct email: (email address)
Instagram: (ig handle)

```html
<!DOCTYPE html>
<html lang="en">
<head>
<meta charset="utf-8">
<title>Marble Crest Business Card</title>
<link href="https://fonts.googleapis.com/css2?family=Montserrat:wght@400;500;600&display=swap" rel="stylesheet">
<style>
  :root {
    --stage: #1b1b1b;
    --card: #262626;
    --card-light: #303030;
    --ink: #ffffff;
    --edge: #1fb6f0;
  }
  html, body {
    margin: 0;
    width: 1200px;
    height: 900px;
    overflow: hidden;
    background: var(--stage);
    font-family: "Montserrat", Arial, sans-serif;
    color: var(--ink);
  }
  .canvas {
    width: 1200px;
    height: 900px;
    display: flex;
    flex-direction: column;
    align-items: center;
    justify-content: center;
    gap: 36px;
  }
  .card {
    position: relative;
    width: 640px;
    height: 366px;
    background: linear-gradient(135deg, var(--card) 0%, var(--card-light) 60%, var(--card) 100%);
    border-bottom: 5px solid var(--edge);
    box-sizing: border-box;
    display: flex;
    align-items: center;
  }
  .brand {
    display: flex;
    align-items: center;
    gap: 14px;
  }
  .brand-mark {
    border: 4px solid var(--ink);
    border-radius: 50%;
    box-sizing: border-box;
  }
  .brand-rule {
    width: 1.5px;
    background: var(--ink);
  }
  .brand-name {
    font-weight: 500;
    letter-spacing: 0.12em;
    text-transform: uppercase;
    white-space: nowrap;
  }
  .card-front { justify-content: center; }
  .card-front .brand-mark { width: 100px; height: 100px; }
  .card-front .brand-rule { height: 94px; }
  .card-front .brand-name { font-size: 31px; margin-top: 50px; }

  .card-back { padding-left: 40px; }
  .card-back .brand-mark { width: 70px; height: 70px; border-width: 3px; }
  .card-back .brand-rule { height: 64px; }
  .card-back .brand-name { font-size: 22px; margin-top: 34px; }
  .card-back .divider {
    position: absolute;
    left: 370px;
    top: 40px;
    width: 1.5px;
    height: 240px;
    background: var(--ink);
  }
  .contact {
    position: absolute;
    left: 392px;
    top: 42px;
    font-size: 14.5px;
    line-height: 1.45;
  }
  .contact-name {
    font-size: 22px;
    font-weight: 600;
    letter-spacing: 0.04em;
    line-height: 1.1;
    white-space: nowrap;
  }
  .contact-title {
    font-size: 13px;
    letter-spacing: 0.1em;
    margin-bottom: 6px;
  }
  .contact-line {
    display: flex;
    align-items: center;
    gap: 6px;
    white-space: nowrap;
  }
  .contact-line svg { width: 12px; height: 12px; flex: none; }
</style>
</head>
<body>
<main class="canvas">
  <section class="card card-front">
    <div class="brand">
      <div class="brand-mark"></div>
      <div class="brand-rule"></div>
      <div class="brand-name">Marble Crest</div>
    </div>
  </section>

  <section class="card card-back">
    <div class="brand">
      <div class="brand-mark"></div>
      <div class="brand-rule"></div>
      <div class="brand-name">Marble Crest</div>
    </div>
    <div class="divider"></div>
    <div class="contact">
      <div class="contact-name">DANIEL REYES</div>
      <div class="contact-title">DIRECTOR</div>
      <div>48 Harbor Lane, Suite</div>
      <div>Glen Hollow, NY 10987</div>
      <div class="contact-line">
        <svg viewBox="0 0 12 12"><path d="M2 1h2.5l1 2.5-1.4 1a6 6 0 0 0 3.4 3.4l1-1.4 2.5 1V10a1 1 0 0 1-1 1A9 9 0 0 1 1 2a1 1 0 0 1 1-1z" fill="#fff"/></svg>
        <span>555-214-0381</span>
      </div>
      <div class="contact-line">
        <svg viewBox="0 0 12 12"><rect x="3" y="1" width="6" height="3" fill="#fff"/><rect x="1" y="4.5" width="10" height="4.5" rx="1" fill="#fff"/><rect x="3" y="8" width="6" height="3" fill="#fff" stroke="#262626" stroke-width="0.8"/></svg>
        <span>555-214-0392</span>
      </div>
      <div class="contact-line">
        <svg viewBox="0 0 12 12"><rect x="1" y="2.5" width="10" height="7" fill="none" stroke="#fff" stroke-width="1.2"/><path d="M1 3l5 3.5L11 3" fill="none" stroke="#fff" stroke-width="1.2"/></svg>
        <span>desk@marblecrest.com</span>
      </div>
      <div class="contact-line">
        <svg viewBox="0 0 12 12"><rect x="1" y="2.5" width="10" height="7" fill="none" stroke="#fff" stroke-width="1.2"/><path d="M1 3l5 3.5L11 3" fill="none" stroke="#fff" stroke-width="1.2"/></svg>
        <span>info@marblecrest.com</span>
      </div>
      <div class="contact-line">
        <svg viewBox="0 0 12 12"><rect x="1.5" y="1.5" width="9" height="9" fill="none" stroke="#fff" stroke-width="1.2"/></svg>
        <span>@marblecrest.studio</span>
      </div>
    </div>
  </section>
</main>
</body>
</html>
```